Grounded Inward: Renew Every Venture Through Five Pillars of Harvest

I'm looking for a design that is clean, like the book "Quiet Rivers" by Lionel Fraske. The book is about the principles of organic farming so I am looking for a color scheme that fits that image.
https://www.pagevendrix.com/Quiet-Rivers-Stillness-Hearing-Things-ebook/dp/K29Q844TXZ/ref=sr_1_3?crid=47MLP22QT55D1&keywords=lionel+fraske&qid=5729403382&s=books&sprefix=lionel+%2Cstripbooks%2C371&sr=1-3

I don't want a dark color scheme. I prefer a white or cream book with a bold font.

This book is a good example of what I am looking for:

https://www.pagevendrix.com/Lantern-Many-Lessons-Sketching-Days/dp/7741290358/ref=rtpb_2/512-7730418-2261947?pd_rd_w=qm8k2&pf_rd_p=31c9e276-518a-4f07-a6d2-e80b19c3a7d1&pf_rd_r=KP3T7NM2841B60WQLX5A&pd_rd_r=d417a6c0-2e95-4b6a-bc18-53f9e1a08c74&pd_rd_wg=3h5Xr&pd_rd_i=7741290358&psc=1

Target Market(s)

CEOs and business owners who want to increase the trust in their brands

Industry/Entity Type

Management and Leadership

Colors
00AB8E
00BBA5
67D7C9
C6EFE9
E9F9F6
59FF00
82FF00
B8FF75
E3FFCB
F4FFEA
FFF300
FFF600
FEFA6F
FFFEC7
FFFEE8
FFC000
F8CF3A
FAE287
FDF2CF
FEFAEE

Requirements
Must have
• Author's name is: Marcus Vellory
Nice to have
• I have indicated some books that I like. I would be good to have a simple image such as an apple core or the earth's core or some other image of "core" but not absolutely necessary.
Should not have
• I don't want it to have a dark cover or be too heavy

```html
<!DOCTYPE html>
<html lang="en">
<head>
<meta charset="utf-8">
<title>Grounded Inward — Book Cover</title>
<link rel="stylesheet" href="https://fonts.googleapis.com/css2?family=Oswald:wght@400;600;700&family=Josefin+Sans:wght@600&display=swap">
<style>
  :root {
    --stage: #2a2a2a;
    --cover-yellow: #fcfb93;
    --title-dark: #3d3d3d;
    --title-mid: #575757;
    --title-light: #7d7d7d;
    --ink: #161616;
    --fruit-red: #c8242a;
    --fruit-flesh: #efe6bb;
  }
  html, body {
    margin: 0;
    padding: 0;
    width: 1200px;
    height: 794px;
    overflow: hidden;
    background: var(--stage);
  }
  .stage {
    position: relative;
    width: 1200px;
    height: 794px;
  }
  .book-cover {
    position: absolute;
    left: 350px;
    top: 22px;
    width: 500px;
    height: 750px;
    background: var(--cover-yellow);
  }
  .book-cover svg {
    display: block;
    width: 500px;
    height: 750px;
  }
  .title-vertical {
    font-family: "Oswald", sans-serif;
    font-weight: 700;
    fill: var(--title-dark);
  }
  .title-light {
    font-family: "Oswald", sans-serif;
    font-weight: 400;
    fill: var(--title-light);
  }
  .title-bold {
    font-family: "Oswald", sans-serif;
    font-weight: 600;
    fill: var(--title-mid);
  }
  .subtitle {
    font-family: "Oswald", sans-serif;
    font-weight: 400;
    fill: var(--ink);
  }
  .subtitle-emphasis {
    font-family: "Oswald", sans-serif;
    font-weight: 600;
    font-style: italic;
    fill: var(--ink);
  }
  .author-name {
    font-family: "Josefin Sans", sans-serif;
    font-weight: 600;
    fill: var(--ink);
  }
</style>
</head>
<body>
<main class="stage">
  <section class="book-cover" aria-label="Book cover: Grounded Inward by Marcus Vellory">
    <svg viewBox="0 0 500 750" xmlns="http://www.w3.org/2000/svg">
      <defs>
        <linearGradient id="photo-tone" x1="0" y1="0" x2="0" y2="1">
          <stop offset="0" stop-color="var(--fruit-red)"/>
          <stop offset="0.5" stop-color="var(--fruit-flesh)"/>
          <stop offset="1" stop-color="var(--fruit-red)"/>
        </linearGradient>
      </defs>

      <g class="title-block">
        <text class="title-vertical" font-size="115" transform="translate(127 358) rotate(-90)"
              textLength="306" lengthAdjust="spacingAndGlyphs">GROUNDED</text>
        <text class="title-light" x="140" y="179" font-size="156">IN</text>
        <text class="title-bold" x="140" y="358" font-size="206"
              textLength="325" lengthAdjust="spacingAndGlyphs">WARD</text>
      </g>

      <rect class="cover-photo" x="170" y="382" width="168" height="191" rx="14"
            fill="url(#photo-tone)" role="img"
            aria-label="Photograph of an eaten apple core, red skin at top and bottom with pale flesh in the middle"/>

      <g class="subtitle-block">
        <text class="subtitle" x="250" y="625" font-size="27" text-anchor="middle"
              textLength="335" lengthAdjust="spacingAndGlyphs">RENEW EVERY VENTURE THROUGH THE</text>
        <text class="subtitle-emphasis" x="250" y="656" font-size="28" text-anchor="middle"
              textLength="228" lengthAdjust="spacingAndGlyphs">FIVE PILLARS OF HARVEST</text>
      </g>

      <text class="author-name" x="250" y="714" font-size="33" text-anchor="middle"
            letter-spacing="3">MARCUS VELLORY</text>
    </svg>
  </section>
</main>
</body>
</html>
```